Assessment Report cover design and formatting

This report is for senior executives and provides leaders with detailed insight into their capabilities and skills. The cover should have space for the date and name of the person doing the assessment. We are looking to modernise the report cover design. We would like the report to be our company colours if possible. The work will likely expand once the cover is done to other parts of the report, ie. the format and layout of the report etc.

Company colours:
Primary colours:
• Blue #0D47A1, #115CD0, #90B6ED, #EEf3FB
• Green #0D91A1, #47A10D, #324C196, #0DA11D
Additional colours:
• Purple #A10D91
• Brown #A1670D
• Red #A10D47

Target Market(s)

Executives

Industry/Entity Type

Consulting, leadership development

Colors
0094D4
00A9DD
6FCCEA
C7EBF8
E9F6FB
00AB8E
00BBA5
67D7C9
C6EFE9
E9F9F6
E54698
E96AAD
F1A4CE
F9D9EA
FCEFF6
6B429C
8869AF
B7A5CE
E3DAEB
F3F0F8

Requirements
Must have
• The report cover should have space for name of user, the date and company logo. Cover should be in A4 size.

```html
<!DOCTYPE html>
<html lang="en">
<head>
<meta charset="utf-8">
<title>Executive Leader Review – Report Cover</title>
<link href="https://fonts.googleapis.com/css2?family=Montserrat:wght@500;700&display=swap" rel="stylesheet">
<style>
  :root {
    --brand-blue: #0D47A1;
    --brand-blue-bright: #115CD0;
    --brand-green: #0DA11D;
    --page: #FFFFFF;
    --backdrop: #9A9B9D;
  }
  * { margin: 0; padding: 0; box-sizing: border-box; }
  html, body {
    width: 1200px;
    height: 1126px;
    overflow: hidden;
    background: var(--backdrop);
    font-family: "Montserrat", sans-serif;
  }
  .report-cover {
    position: absolute;
    left: 175px;
    top: 33px;
    width: 850px;
    height: 1060px;
    background: var(--page);
    overflow: hidden;
  }
  .cover-art {
    position: absolute;
    left: 0;
    top: 0;
    width: 850px;
    height: 790px;
    background:
      linear-gradient(to bottom, rgba(255,255,255,0) 0%, rgba(255,255,255,0) 82%, #FFFFFF 100%),
      linear-gradient(135deg, #4FA0D8 0%, #4FC3C4 30%, #78B5C4 50%, #5A78D6 70%, #4CBFCB 100%);
  }
  .header-band {
    position: absolute;
    left: 0;
    top: 0;
    width: 850px;
    height: 44px;
    background: var(--brand-blue);
  }
  .header-rule {
    position: absolute;
    left: 0;
    top: 50px;
    width: 850px;
    height: 8px;
    background: var(--brand-green);
  }
  .title-plate {
    position: absolute;
    left: 0;
    top: 108px;
    width: 409px;
    height: 99px;
    background: var(--page);
    border-radius: 0 5px 5px 0;
    padding: 6px 0 0 11px;
  }
  .title-main {
    font-weight: 700;
    font-size: 44px;
    line-height: 48px;
    color: var(--brand-blue);
    white-space: nowrap;
  }
  .title-sub {
    font-weight: 500;
    font-size: 41px;
    line-height: 40px;
    color: var(--brand-green);
    padding-left: 4px;
  }
  .recipient {
    position: absolute;
    left: 33px;
    top: 818px;
    color: var(--brand-blue);
  }
  .recipient-label { font-size: 19px; font-weight: 500; }
  .recipient-name { font-size: 19px; font-weight: 700; margin: 14px 0 0 33px; letter-spacing: 0.5px; }
  .report-date { font-size: 19px; font-weight: 500; margin: 31px 0 0 19px; }
  .company-name {
    position: absolute;
    left: 500px;
    top: 832px;
    display: flex;
    align-items: center;
    gap: 16px;
    color: var(--brand-blue);
    font-weight: 500;
    font-size: 40px;
    line-height: 46px;
  }
  .company-dot {
    width: 34px;
    height: 34px;
    border-radius: 50%;
    background: var(--brand-blue-bright);
    flex: none;
  }
  .confidential {
    position: absolute;
    left: 0;
    width: 814px;
    top: 985px;
    text-align: center;
    font-size: 16px;
    font-weight: 500;
    color: var(--brand-blue);
    letter-spacing: 0.3px;
  }
  .footer-rule {
    position: absolute;
    left: 0;
    top: 1016px;
    width: 850px;
    height: 8px;
    background: var(--brand-blue);
  }
  .footer-band {
    position: absolute;
    left: 0;
    top: 1030px;
    width: 850px;
    height: 30px;
    background: var(--brand-green);
  }
</style>
</head>
<body>
  <main class="report-cover">
    <div class="cover-art" role="img" aria-label="Abstract layered blue and teal square panels"></div>
    <div class="header-band"></div>
    <div class="header-rule"></div>

    <header class="title-plate">
      <h1 class="title-main">Executive Leader</h1>
      <p class="title-sub">Review</p>
    </header>

    <section class="recipient">
      <p class="recipient-label">INSIGHT REPORT FOR</p>
      <p class="recipient-name">ALEX MORGAN</p>
      <p class="report-date">October 03, 2023</p>
    </section>

    <div class="company-name">
      <span class="company-dot"></span>
      <span>Meridian<br>Partners</span>
    </div>

    <p class="confidential">CONFIDENTIAL</p>
    <div class="footer-rule"></div>
    <div class="footer-band"></div>
  </main>
</body>
</html>
```